Lumen Cove Skincare - Package Design

New Beauty label needing product packaging design. Looking for elegant and stylish design to represent our premium brand.

This project is for 1 label and 1 box design. The winning designer will be assigned another project for the next product in the range. (to be paid as a new project)

This product is for "Dead Sea Mud Mask". Please see the label format and jar attached. Please note there are 2 different jars we are considering (will have a mud inside). Please feel free to choose whichever one suits your design best.

The labels and boxes are to retain the product information, such as size, ingredients etc, but is to be updated to our brand. You can move or display the other information as you wish.

the size of the dead sea mud mask color box is 72*72*85mm (length*width*height)
the size of dead sea mud mask label is 218*58mm (width*height)

Target Market(s)

Women 15 to 65

Requirements
Must have
• Must be elegant and represent our brand which is a premium beauty product.
Should not have
• Dark blue. Dark purple etc. Colours should compliment the logo

```html
<!DOCTYPE html>
<html lang="en">
<head>
<meta charset="utf-8">
<title>Lumen Cove Skincare – Dead Sea Mud Mask Label</title>
<link rel="stylesheet" href="https://fonts.googleapis.com/css2?family=Playfair+Display:wght@700&family=Montserrat:ital,wght@1,500&display=swap">
<style>
  :root {
    --page-bg: #ffffff;
    --label-bg: #eeeeee;
    --label-edge: #dddddd;
    --gold: #9a7424;
    --gold-deep: #7d5c17;
    --wave-soft: #b7cedd;
    --wave-mist: #d6e3ec;
    --wave-pale: #e8eff4;
  }
  html, body {
    margin: 0;
    width: 1200px;
    height: 961px;
    overflow: hidden;
    background: var(--page-bg);
  }
  .label {
    position: absolute;
    left: 220px;
    top: 130px;
    width: 760px;
    height: 700px;
    background: var(--label-bg);
    border: 1px solid var(--label-edge);
    overflow: hidden;
    box-sizing: border-box;
  }
  .brand {
    position: absolute;
    left: 0;
    right: 0;
    top: 168px;
    display: flex;
    align-items: center;
    justify-content: center;
    gap: 14px;
  }
  .brand-dot {
    width: 16px;
    height: 16px;
    border: 2px solid var(--gold);
    border-radius: 50%;
    box-sizing: border-box;
  }
  .brand-name {
    font-family: "Playfair Display", serif;
    font-weight: 700;
    font-size: 44px;
    line-height: 56px;
    color: var(--gold);
  }
  .wave-art {
    position: absolute;
    left: 0;
    right: 0;
    top: 380px;
    bottom: 0;
    background:
      radial-gradient(ellipse 70% 90% at 50% 100%, var(--wave-soft) 0%, var(--wave-mist) 55%, transparent 100%),
      linear-gradient(to bottom, var(--label-bg) 0%, var(--wave-pale) 40%, var(--wave-mist) 100%);
  }
  .product-title {
    position: absolute;
    left: 0;
    right: 0;
    top: 400px;
    margin: 0;
    text-align: center;
    font-family: "Playfair Display", serif;
    font-weight: 700;
    font-size: 52px;
    line-height: 64px;
    color: var(--gold);
  }
  .product-claim {
    position: absolute;
    left: 0;
    right: 0;
    top: 506px;
    margin: 0;
    text-align: center;
    font-family: "Montserrat", sans-serif;
    font-style: italic;
    font-weight: 500;
    font-size: 24px;
    line-height: 38px;
    color: var(--gold-deep);
  }
  .product-size {
    position: absolute;
    left: 0;
    right: 0;
    top: 612px;
    margin: 0;
    text-align: center;
    font-family: "Montserrat", sans-serif;
    font-style: italic;
    font-weight: 500;
    font-size: 24px;
    line-height: 32px;
    color: var(--gold-deep);
  }
</style>
</head>
<body>
  <main class="label">
    <div class="brand">
      <span class="brand-dot"></span>
      <span class="brand-name">Lumen Cove Skincare</span>
    </div>
    <div class="wave-art" role="img" aria-label="Soft splashing sea wave illustration"></div>
    <h1 class="product-title">DEAD SEA MUD MASK</h1>
    <p class="product-claim">Acne, Pores, Blackheads,<br>Whiteheads and Breakouts</p>
    <p class="product-size">250g · 8.8 fl. Oz</p>
  </main>
</body>
</html>
```